Design a Small Graphic for a client brochure and Website

We need a a fairly simple diagram/graphic to replace the existing graphic in our brochures and website. We are a Private Wealth Advice firm, dealing with high-end clients. We would like to be able to copyright the final design. We need this design to be stylish and have a long shelf-life.
The original design is quite old and was not updated to reflect our company growth or changes in our website design and brochure designs.
Updates

Target Market(s)

Private Wealth clients
High end
Age 45 plus

Industry/Entity Type

Finance

Font styles to use
Sans Serif
Other font styles liked:
• Stag Sans

Requirements
Must have
• Corporate colours only - plus white
• Pantone 288c (Blue)
• Pantone Cool grey 10c
• Pantone 666c (purple - only limited use for highlighting etc)
• Corporate fonts only
• Stag Sans light, book and thin
• Must provide AI editable files
• Must be able to scale to size and remove/replace any text
• Must be in keeping with our brochures and website which can be viewed at www.lorvane-advisory.com.au
Nice to have
• We want something more vibrant than the image we are using. Something which is in keeping with our image but that is really eye catching.

```html
<!DOCTYPE html>
<html lang="en">
<head>
<meta charset="utf-8">
<title>Advice Framework Diagram</title>
<link rel="stylesheet" href="https://fonts.googleapis.com/css2?family=Roboto:wght@400&display=swap">
<style>
  :root {
    --blue: #124b8a;
    --grey: #807f84;
    --lavender: #a5a3c8;
    --white: #ffffff;
    --edge: #8c8c8e;
    --ink: #231f20;
    --hub-edge: #e6e8ef;
  }
  html, body {
    margin: 0;
    padding: 0;
    width: 1198px;
    height: 1200px;
    overflow: hidden;
    background: var(--white);
  }
  .framework {
    display: block;
    width: 1198px;
    height: 1200px;
  }
  .piece { stroke: var(--white); stroke-width: 8; stroke-linejoin: round; }
  .piece--purpose { fill: var(--blue); }
  .piece--investment { fill: var(--grey); }
  .piece--legacy { fill: var(--lavender); }
  .piece--wealth { fill: var(--white); stroke: var(--edge); stroke-width: 3; }
  .knob-shape { stroke: var(--white); stroke-width: 8; stroke-linejoin: round; stroke-linecap: round; }
  .knob--purpose { fill: var(--blue); }
  .knob--investment { fill: var(--grey); }
  .knob--legacy { fill: var(--lavender); }
  .knob--wealth { fill: var(--white); }
  .knob--wealth .knob-shape { stroke: var(--edge); stroke-width: 3; }
  .hub-mark { stroke: var(--edge); stroke-width: 2; }
  .label {
    font-family: "Roboto", "Helvetica Neue", Arial, sans-serif;
    font-weight: 400;
    font-size: 112px;
    text-anchor: middle;
  }
  .label--light { fill: var(--white); }
  .label--dark { fill: var(--ink); }
</style>
</head>
<body>
<svg class="framework" viewBox="0 0 1440 1440" xmlns="http://www.w3.org/2000/svg" role="img" aria-label="Four-part advice framework: Purpose, Investment Consulting, Your Legacy, Wealth Planning">
  <defs>
    <filter id="lift" x="-10%" y="-10%" width="120%" height="120%">
      <feDropShadow dx="0" dy="3" stdDeviation="4" flood-color="#000" flood-opacity="0.35"/>
    </filter>
    <radialGradient id="hub-fill" cx="50%" cy="50%" r="50%">
      <stop offset="0%" stop-color="#ffffff"/>
      <stop offset="100%" stop-color="#e6e8ef"/>
    </radialGradient>
    <path id="knob" class="knob-shape" d="M0,-22 Q-22,-22 -30,-30 A44,44 0 1 0 -30,30 Q-22,22 0,22"/>
  </defs>

  <g class="ring" filter="url(#lift)">
    <path class="piece piece--purpose" d="M15,723 A705,705 0 0 1 720,18 L720,498 A225,225 0 0 0 495,723 Z"/>
    <path class="piece piece--investment" d="M720,18 A705,705 0 0 1 1425,723 L945,723 A225,225 0 0 0 720,498 Z"/>
    <path class="piece piece--legacy" d="M1425,723 A705,705 0 0 1 720,1428 L720,948 A225,225 0 0 0 945,723 Z"/>
    <path class="piece piece--wealth" d="M720,1428 A705,705 0 0 1 15,723 L495,723 A225,225 0 0 0 720,948 Z"/>

    <g class="knob knob--investment" transform="translate(720,255)">
      <use href="#knob"/>
      <rect x="-6" y="-18" width="12" height="36"/>
    </g>
    <g class="knob knob--legacy" transform="translate(1180,723) rotate(90)">
      <use href="#knob"/>
      <rect x="-6" y="-18" width="12" height="36"/>
    </g>
    <g class="knob knob--wealth" transform="translate(720,1190) rotate(180)">
      <use href="#knob"/>
      <rect x="-6" y="-20" width="12" height="40"/>
    </g>
    <g class="knob knob--purpose" transform="translate(255,723) rotate(-90)">
      <use href="#knob"/>
      <rect x="-6" y="-18" width="12" height="36"/>
    </g>
  </g>

  <g class="hub" role="img" aria-label="Central pointer mark in blue and grey">
    <circle class="hub-mark" cx="720" cy="723" r="221" fill="url(#hub-fill)"/>
  </g>

  <text class="label label--light" x="397" y="415" textLength="385" lengthAdjust="spacingAndGlyphs">Purpose</text>
  <text class="label label--dark" x="1012" y="365" textLength="455" lengthAdjust="spacingAndGlyphs">Investment</text>
  <text class="label label--dark" x="1010" y="462" textLength="440" lengthAdjust="spacingAndGlyphs">Consulting</text>
  <text class="label label--dark" x="1040" y="1022" textLength="200" lengthAdjust="spacingAndGlyphs">Your</text>
  <text class="label label--dark" x="1038" y="1120" textLength="295" lengthAdjust="spacingAndGlyphs">Legacy</text>
  <text class="label label--dark" x="400" y="1020" textLength="285" lengthAdjust="spacingAndGlyphs">Wealth</text>
  <text class="label label--dark" x="402" y="1118" textLength="360" lengthAdjust="spacingAndGlyphs">Planning</text>
</svg>
</body>
</html>
```